Skill Up Salary Up

Full Page
7.5 w x 10 h / 8 w x 10.75 h + .25" bleed
Full-Page Career Course Ad
Project Overview
• Goal: Create a visually attractive, modern, and uncluttered full-page magazine advertisement to list available career courses.
• Tone: Creative, professional, and attention-grabbing to prevent the reader from turning the page. The final design must prioritize readability.

Content Requirements
1. Header/Headline: Must be the primary focus. And grab peoples attention
2. Course Listing: A clear, well-organized list of the career courses.
________________________________________
Design & Aesthetic Directives
1. Layout & Readability (Crucial)
• The final ad must not look crowded or busy.
• Prioritize white space to make the text "breathe" and ensure the course list is easy to scan and read.
• Use a modern, clean, and professional typeface (font choice is critical for the aesthetic).
2. Visual Style
• Aim for a creative, modern, and fresh look. Avoid outdated or generic stock imagery/layouts.
3. Imagery/Graphic Element (Artist's Choice)
You have creative freedom regarding the main graphic element.
• Option A (Photography): Use a photo of a white male American with a collared shirt. The imagery should convey success, focus, or professional development.
• Option B (Vector/Illustration): Use a modern vector graphic, illustration, or abstract design. This could be used to symbolize growth, connection, or a career path.
The choice of graphic element is yours, but it must support the overall modern and uncrowded aesthetic.

Requirements
Must have
• Partial listing .. is part of the Harbor Lantern Course

```html
<!DOCTYPE html>
<html lang="en">
<head>
<meta charset="utf-8">
<title>Skill Up, Salary Up – Upcoming Kestrel Courses</title>
<link href="https://fonts.googleapis.com/css2?family=Inter:ital,wght@0,300;0,400;0,700;0,800;0,900;1,200;1,300;1,800;1,900&display=swap" rel="stylesheet">
<style>
  :root {
    --ink: #000000;
    --paper: #ffffff;
    --sky-light: #eef5fb;
    --sky-mid: #dbe9f4;
    --rule: #9a9a9a;
    --photo-shirt: #e9eef2;
    --photo-skin: #c99a80;
  }
  * { margin: 0; padding: 0; box-sizing: border-box; }
  html, body { width: 893px; height: 1200px; overflow: hidden; background: var(--paper); }
  body { font-family: "Inter", Arial, sans-serif; color: var(--ink); }
  .ad {
    position: relative; width: 893px; height: 1200px; overflow: hidden;
    border: 1px solid var(--ink); background: var(--paper);
  }
  .hero-backdrop {
    position: absolute; left: 0; top: 0; width: 893px; height: 480px;
    background: linear-gradient(180deg, var(--sky-mid) 0%, var(--sky-light) 60%, var(--paper) 100%);
  }
  .hero-photo {
    position: absolute; right: 0; top: 32px; width: 360px; height: 440px;
    background: radial-gradient(ellipse at 62% 40%, var(--photo-skin) 0%, var(--photo-shirt) 38%, rgba(233,238,242,0) 75%);
  }
  .headline { position: absolute; left: 50px; top: 44px; line-height: 1; }
  .headline-light {
    display: block; font-weight: 200; font-style: italic; font-size: 80px;
    letter-spacing: 1px; line-height: 76px;
  }
  .headline-bold {
    display: block; font-weight: 900; font-style: italic; font-size: 76px;
    letter-spacing: -1.5px; line-height: 76px; margin-top: 2px;
  }
  .features { position: absolute; left: 50px; top: 360px; list-style: none; }
  .features li { font-size: 25px; font-weight: 300; letter-spacing: 1px; line-height: 30px; }
  .features li::before { content: "•"; margin-right: 12px; font-size: 18px; vertical-align: 3px; }
  .courses {
    position: absolute; left: 49px; top: 493px; width: 795px; height: 424px;
    display: grid; grid-template-columns: 193px 204px 204px 194px;
    border-bottom: 1px solid var(--rule);
  }
  .course { position: relative; padding-left: 25px; border-left: 1px solid var(--rule); }
  .course:first-child { padding-left: 0; border-left: none; }
  .course-title { font-size: 28px; font-weight: 800; line-height: 30px; letter-spacing: -0.3px; }
  .course-tagline { font-size: 17px; font-weight: 800; line-height: 22px; margin-top: 20px; }
  .course-tagline small { display: block; font-size: 14px; }
  .checklist { list-style: none; margin-top: 16px; }
  .checklist li { font-size: 15.5px; font-weight: 300; line-height: 19px; padding-left: 14px; text-indent: -14px; margin-bottom: 6px; }
  .checklist li::before { content: "✓"; display: inline-block; width: 14px; text-indent: 0; }
  .check-label { font-size: 15px; font-weight: 800; margin-top: 20px; }
  .check-label + .checklist { margin-top: 0; }
  .note { font-size: 15px; line-height: 19px; margin-top: 18px; }
  .note strong { font-weight: 800; display: block; }
  .note span { font-weight: 300; }
  .course-date {
    position: absolute; bottom: 14px; left: 25px;
    font-size: 28px; font-weight: 900; line-height: 30px;
  }
  .course:first-child .course-date { left: 0; }
  .enrichment { position: absolute; left: 108px; top: 926px; width: 690px; }
  .enrichment-name { font-size: 42px; font-weight: 900; font-style: italic; letter-spacing: -0.5px; line-height: 44px; }
  .enrichment-sub { font-size: 28px; font-weight: 200; font-style: italic; letter-spacing: 1.5px; line-height: 34px; }
  .enrichment-list { font-size: 15.5px; font-weight: 300; line-height: 21px; margin-top: 6px; letter-spacing: 0.2px; white-space: nowrap; }
  .enrichment-list strong { font-weight: 800; }
  .duration-badge { position: absolute; left: 678px; top: 933px; width: 106px; height: 92px; }
  .outcomes {
    position: absolute; left: 49px; top: 1060px; width: 795px; height: 28px;
    border-bottom: 1px solid var(--rule); display: flex;
  }
  .outcomes span { font-size: 15px; font-weight: 800; line-height: 18px; }
  .outcomes span:nth-child(1) { width: 290px; padding-left: 59px; }
  .outcomes span:nth-child(2) { width: 208px; padding-left: 33px; border-left: 1px solid var(--rule); }
  .outcomes span:nth-child(3) { padding-left: 35px; border-left: 1px solid var(--rule); }
</style>
</head>
<body>
<main class="ad">
  <div class="hero-backdrop"></div>
  <div class="hero-photo" role="img" aria-label="Photo of a smiling professional man in a white collared shirt and striped tie, seated at a laptop"></div>

  <h1 class="headline">
    <span class="headline-light">SKILL UP,</span>
    <span class="headline-light">SALARY UP</span>
    <span class="headline-bold">UPCOMING</span>
    <span class="headline-bold">KESTREL COURSES</span>
  </h1>

  <ul class="features">
    <li>MEN &amp; WOMEN</li>
    <li>IN-PERSON &amp; REMOTE</li>
    <li>PARTIAL SCHOLARSHIPS</li>
  </ul>

  <section class="courses">
    <article class="course">
      <h2 class="course-title">Software,<br>Web &amp; Apps</h2>
      <p class="course-tagline">#2 Best Tech Job National Career Digest 2025<small>Job Opportunities</small></p>
      <ul class="checklist">
        <li>Computer Programmer</li>
        <li>Software Developer / Mobile</li>
        <li>Engineer Developer (Apps)</li>
      </ul>
      <p class="note"><strong>Optional:</strong><span>Bachelors in Prog. &amp; Tech</span></p>
      <p class="course-date">NOV 2025</p>
    </article>
    <article class="course">
      <h2 class="course-title">Book-<br>keeping<br>LedgerPro</h2>
      <p class="course-tagline">Train for a quality job Manage your own books</p>
      <ul class="checklist">
        <li>Finance Management</li>
        <li>Customer &amp; Vendor Mgmt.</li>
        <li>Advanced Tools</li>
      </ul>
      <p class="course-date">5 WEEKS<br>NOV 2025</p>
    </article>
    <article class="course">
      <h2 class="course-title">IT Desktop &amp; Networking Support</h2>
      <p class="course-tagline">#2 Best Job National Career Digest 2025</p>
      <p class="check-label">Masters IT:</p>
      <ul class="checklist">
        <li>DeskOS</li>
        <li>Networks</li>
        <li>Servers</li>
        <li>Cloud</li>
      </ul>
      <p class="course-date">7 MONTHS<br>DEC 2025</p>
    </article>
    <article class="course">
      <h2 class="course-title">Desktop Office-<br>Computers</h2>
      <p class="course-tagline">The New Job Prerequisite</p>
      <ul class="checklist">
        <li>CellGrid</li>
        <li>DocWriter</li>
        <li>MailDesk</li>
        <li>SlideDeck</li>
      </ul>
      <p class="note"><strong>Computer lab available to practice</strong></p>
      <p class="course-date">5 WEEKS<br>DEC 2025</p>
    </article>
  </section>

  <section class="enrichment">
    <h2 class="enrichment-name">HARBOR LANTERN</h2>
    <p class="enrichment-sub">BUSINESS SKILLS &amp; KNOWLEDGE TO:</p>
    <p class="enrichment-list"><strong>PARTIAL LISTING</strong> Computers / Marketing / Sales / Finance / Healthcare /<br>Business Strategy Communication / LedgerPro / Investments / Real Estate / Accounting</p>
  </section>

  <svg class="duration-badge" viewBox="0 0 106 92" aria-label="4-5 months, starting November 2025">
    <polygon points="26,0 80,0 106,46 80,92 26,92 0,46" fill="#000"/>
    <text x="53" y="22" fill="#fff" font-family="Inter, Arial, sans-serif" font-size="11" font-weight="300" text-anchor="middle">4-5</text>
    <text x="53" y="36" fill="#fff" font-family="Inter, Arial, sans-serif" font-size="11" font-weight="300" text-anchor="middle">MONTHS</text>
    <text x="53" y="63" fill="#fff" font-family="Inter, Arial, sans-serif" font-size="24" font-weight="900" text-anchor="middle">NOV</text>
    <text x="53" y="81" fill="#fff" font-family="Inter, Arial, sans-serif" font-size="15" font-weight="800" text-anchor="middle">2025</text>
  </svg>

  <div class="outcomes">
    <span>Impress your interviewer</span>
    <span>Maximize Income</span>
    <span>Start / Run Your Business</span>
  </div>
</main>
</body>
</html>
```